A.I. technology startup needs a website design

We need a website design for our artificial intelligence product vkMender.
vkMender is a platform that uses the latest advances in natural language processing and machine learning to intelligently communicate to users and provide users an interface to interact with organizations through natural language. It is designed as a contact centre robot that automates the handling of customer service inquiries, thus helping to improve service quality and reduce operational expenses. Unlike any other artificial intelligence, this system is trained by using a knowledgebase combined with on-the-job training to quickly learn answers to frequently asked questions and be able to provide intelligent responses to user inquiries.
We would like this product website to show prospective customers what vkMender is about and to generate excitement for this product, as we are in the middle of launching out worldwide.
----------------------------------------------
The website design should be modern and clean. Our product uses cutting edge technology and we want the website to deliver this message.
We like modern style websites with large fonts and images and dynamic design.
There should be a menu at the top with the following options which will navigate the user to the appropriate page:
- vkMender (this acts as the home page)
- Benefits
- How It Works
- About Us
The website should be responsive for mobile device users.
Here are some examples of website designs we like:
http://www.plumvaro.com/
https://www.quillharborinc.com
https://www.bravolume.com/customer-support-software
https://www.fintorra.com/
We have some attachments which may help in the website. Please take a look at our existing material, which includes: vkMender logo, vkMender powerpoint presentation (contains alot of content we can re-use on the website), and more.
Appreciate your creative talent and website expertise, and we look forward to seeing your designs!

```html
<!DOCTYPE html>
<html lang="en">
<head>
<meta charset="utf-8">
<title>About vkMender</title>
<link rel="stylesheet" href="https://fonts.googleapis.com/css2?family=Montserrat:wght@300;400;500&display=swap">
<style>
  :root {
    --hero-blue: #0a82cf;
    --hero-blue-deep: #0674bd;
    --accent: #22b5ee;
    --page: #f4f6f8;
    --band: #e1e9ec;
    --ink: #3a3f45;
    --muted: #6c7278;
    --soft: #9aa1a7;
    --line: #c9ced3;
    --white: #ffffff;
    --leaf: #7ab648;
    --brand-dark: #1d3f7a;
  }
  * { box-sizing: border-box; margin: 0; padding: 0; }
  html, body { width: 983px; height: 1200px; overflow: hidden; }
  body {
    position: relative;
    background: var(--page);
    font-family: "Montserrat", Arial, sans-serif;
    color: var(--ink);
  }

  /* Hero */
  .hero {
    position: absolute; left: 0; top: 0; width: 983px; height: 262px;
    background: var(--hero-blue);
  }
  .hero-pattern {
    position: absolute; inset: 0;
    background:
      radial-gradient(ellipse 300px 220px at 120px 140px, rgba(255,255,255,0.06), transparent 70%),
      radial-gradient(ellipse 320px 240px at 880px 150px, rgba(255,255,255,0.06), transparent 70%),
      linear-gradient(180deg, var(--hero-blue) 0%, var(--hero-blue-deep) 100%);
  }
  .brand {
    position: absolute; left: 66px; top: 40px;
    display: flex; align-items: center; gap: 10px;
    color: var(--white); font-weight: 300; font-size: 26px; letter-spacing: 0.2px;
  }
  .brand-dot { width: 30px; height: 30px; border-radius: 50%; background: var(--white); opacity: 0.9; }
  .main-nav a {
    position: absolute; top: 54px;
    color: var(--white); text-decoration: none;
    font-size: 10.5px; font-weight: 400; letter-spacing: 0.4px;
  }
  .main-nav a.is-current { color: var(--accent); }
  .contact-btn {
    position: absolute; left: 800px; top: 46px; width: 117px; height: 27px;
    border: 1.5px solid var(--accent); border-radius: 14px;
    color: var(--white); font-size: 10.5px; letter-spacing: 0.6px;
    display: flex; align-items: center; justify-content: center;
  }
  .page-title {
    position: absolute; left: 0; width: 983px; top: 147px; text-align: center;
    color: var(--white); font-weight: 300; font-size: 24px;
  }
  .breadcrumb {
    position: absolute; left: 0; width: 983px; top: 183px; text-align: center;
    color: var(--white); font-size: 10px; letter-spacing: 0.6px;
  }
  .breadcrumb .current { color: var(--accent); }

  /* Intro */
  .intro-lead {
    position: absolute; left: 127px; top: 312px; width: 340px;
    font-size: 15.5px; font-weight: 300; line-height: 22.5px; color: var(--muted);
  }
  .intro-body {
    position: absolute; left: 501px; top: 313px; width: 350px;
    font-size: 11px; font-weight: 400; line-height: 15.8px; color: var(--muted);
    text-align: justify; hyphens: auto;
  }
  .intro-body p + p { margin-top: 16px; }
  .intro-body p.more { margin-top: 32px; text-align: left; }
  .intro-body a { color: var(--muted); text-decoration: underline; }

  /* Clients */
  .clients {
    position: absolute; left: 0; top: 630px; width: 983px; height: 131px;
    background: var(--band);
  }
  .client {
    position: absolute; top: 50px; display: flex; align-items: center; gap: 8px;
    font-size: 24px; font-weight: 500; color: var(--brand-dark);
  }
  .client-mark { width: 22px; height: 22px; border-radius: 50%; background: var(--leaf); }

  /* Contact */
  .eyebrow {
    position: absolute; left: 0; width: 983px; top: 812px; text-align: center;
    font-size: 9.5px; letter-spacing: 1.2px; color: var(--soft);
  }
  .section-title {
    position: absolute; left: 0; width: 983px; top: 833px; text-align: center;
    font-size: 24px; font-weight: 300; color: var(--ink);
  }
  .section-title em { font-style: normal; font-weight: 500; color: var(--accent); }
  .field {
    position: absolute; border: 1px solid var(--line); border-radius: 3px;
    background: var(--page); font-size: 10.5px; color: var(--soft);
    padding: 8px 13px;
  }
  .send-btn {
    position: absolute; left: 432px; top: 1062px; width: 118px; height: 26px;
    border: 1.5px solid var(--accent); border-radius: 13px;
    display: flex; align-items: center; justify-content: center;
    font-size: 10px; letter-spacing: 0.8px; color: var(--ink);
  }

  /* Footer */
  .footer-brand {
    position: absolute; left: 127px; top: 1133px;
    font-size: 26px; font-weight: 400; color: var(--ink);
  }
  .copyright {
    position: absolute; left: 252px; top: 1151px;
    font-size: 10.5px; letter-spacing: 0.6px; color: var(--soft);
  }
  .copyright .company { color: var(--leaf); }
  .footer-nav a {
    position: absolute; top: 1151px;
    font-size: 10.5px; letter-spacing: 0.4px; color: var(--soft); text-decoration: none;
  }
  .footer-nav a.is-active { color: var(--accent); }
  .bookmark { position: absolute; left: 844px; top: 1142px; }
</style>
</head>
<body>

<header class="hero">
  <div class="hero-pattern" role="img" aria-label="Faint circuit-board line pattern across the blue header"></div>
  <div class="brand"><span class="brand-dot"></span>vkMender</div>
  <nav class="main-nav">
    <a style="left:424px">VKMENDER</a>
    <a style="left:514px">BENEFITS</a>
    <a style="left:593px">HOW IT WORKS</a>
    <a class="is-current" style="left:705px">ABOUT US</a>
  </nav>
  <div class="contact-btn">CONTACT US</div>
  <h1 class="page-title">About vkMender</h1>
  <div class="breadcrumb">HOME &nbsp;/&nbsp; <span class="current">ABOUT US</span></div>
</header>

<section>
  <p class="intro-lead">vkMender is an enterprise chatbot<br>platform, designed to automate frequent<br>customer dialogues in chat<br>environments – ranging from SMS to<br>mobile web.</p>
  <div class="intro-body">
    <p>vkMender uses the latest in natural language processing (NLP) and machine learning technology to enable excellent customer experience, smooth operator experience and meaningful bottom line impact.</p>
    <p>vkMender is technology owned by Tavrin Limited. Founded in 2011, Tavrin Limited is a leader in artificial intelligence for customer service. The company is specialized in automation and business intelligence and has a 25 year history serving leading organizations including Halden Telecom, Paylisk and Ardent Auto Club. Most recently, Tavrin launched vkMender – a cutting-edge enterprise chatbot platform designed to meet the next-generation customer service needs of top organizations.</p>
    <p class="more">For more information about us, please visit<br><a>www.tavrinlimited.com</a></p>
  </div>
</section>

<section class="clients">
  <div class="client" style="left:272px">Halden</div>
  <div class="client" style="left:420px">Paylisk <span class="client-mark"></span></div>
  <div class="client" style="left:604px">Ardent</div>
</section>

<section>
  <div class="eyebrow">GET IN TOUCH</div>
  <h2 class="section-title">Drop <em>us</em> a message</h2>
  <div class="field" style="left:190px;top:890px;width:295px;height:27px;padding-top:7px">Name</div>
  <div class="field" style="left:498px;top:890px;width:295px;height:27px;padding-top:7px">Email</div>
  <div class="field" style="left:190px;top:930px;width:603px;height:98px">Type your Message</div>
  <div class="send-btn">SEND</div>
</section>

<footer>
  <div class="footer-brand">Tavrin</div>
  <div class="copyright">© 2017 <span class="company">TAVRIN</span> LIMITED</div>
  <nav class="footer-nav">
    <a style="left:470px">VKMENDER</a>
    <a class="is-active" style="left:556px">BENEFITS</a>
    <a style="left:637px">HOW IT WORKS</a>
    <a style="left:746px">ABOUT US</a>
  </nav>
  <svg class="bookmark" width="12" height="18" viewBox="0 0 12 18" aria-hidden="true">
    <path d="M1 1 H11 V17 L6 12 L1 17 Z" fill="none" stroke="#8a9096" stroke-width="1.2" stroke-linejoin="round"/>
  </svg>
</footer>

</body>
</html>
```